Global Yoga Apparel Brand Needs a Beautiful Website

We need a website design for a new Yoga brand called Vessa. We develop beautiful, stylish, sexy, comfortable yoga leggings, tops, and yoga apparel for women looking to feel their best, look their best and perform their best on and off the yoga mat.
This will go up at http://vessa.example/ (which is a landing page right now).
We would like to see simple and clean design where the focus will be on powerful images and clean background space. We will be using Shopify to start building on and here are three sites that we would love to see options based off of the look, layout and feel while making something unique at the same time:
1. Tumo.ca
2. marikoven.com
3. www.q-plume.com
The final design should look clean, beautiful, inspiring, powerful and empowering.
Target Market(s)
mostly Females 21-35 range but will be appealing to women over 35 as well.

```html
<!DOCTYPE html>
<html lang="en">
<head>
<meta charset="utf-8">
<title>Vessa — Yoga Apparel</title>
<link rel="stylesheet" href="https://fonts.googleapis.com/css2?family=Josefin+Sans:wght@300;400;700&family=Lato:wght@400;700&family=Roboto:wght@300;400&display=swap">
<style>
:root{
  --ink:#111;
  --paper:#fff;
  --hero-a:#ececf0;
  --hero-b:#d9d9de;
  --card:#e9e9eb;
  --card-band:rgba(255,255,255,.55);
  --muted:#444;
  --footer:#3b3b3d;
  --footer-deep:#2b2b2d;
  --footer-text:#d8d8d8;
  --social:#5b86c5;
  --social-alt:#c9574b;
}
*{box-sizing:border-box;margin:0;padding:0}
html,body{width:776px;height:1200px;overflow:hidden;background:var(--paper)}
body{position:relative;font-family:"Lato",sans-serif;color:var(--ink)}
.abs{position:absolute}

/* hero */
.hero{left:0;top:0;width:776px;height:361px;background:linear-gradient(100deg,var(--hero-b) 0%,var(--hero-a) 55%,var(--hero-b) 100%)}
.hero-photo{left:70px;top:10px;width:420px;height:300px;border-radius:50% 40% 20% 20%;background:radial-gradient(ellipse at 45% 55%,#c9a68e 0%,#b99a86 35%,rgba(217,217,222,0) 70%)}
.brand{left:64px;top:8px;font-family:"Josefin Sans",sans-serif;font-weight:700;font-size:34px;letter-spacing:-1px;color:var(--ink)}
.cart-link{left:560px;top:25px;font-family:"Lato",sans-serif;font-size:12px;display:flex;align-items:center;gap:10px}
.menu{left:683px;top:25px}
.offer{left:418px;top:92px;width:280px;text-align:center;font-family:"Josefin Sans",sans-serif;font-weight:300;color:var(--ink)}
.offer .pct{font-size:46px;line-height:46px}
.offer .pct small{font-size:16px}
.offer .line{font-size:28px;line-height:36px}
.buy{left:518px;top:217px;width:80px;height:22px;background:var(--ink);color:#fff;font-family:"Lato",sans-serif;font-weight:700;font-size:11px;display:flex;align-items:center;justify-content:center}
.dots span{position:absolute;top:340px;height:3px;width:22px;background:var(--ink)}
.dots span.on{height:4px}

/* featured */
.section-title{left:64px;top:390px;font-family:"Josefin Sans",sans-serif;font-size:23px;font-weight:400}
.title-rule{left:66px;top:425px;width:35px;height:2px;background:var(--ink)}
.pager{top:403px;width:15px;height:15px;border:1px solid var(--ink);display:flex;align-items:center;justify-content:center}
.product{background:linear-gradient(180deg,#f4f4f5,var(--card));overflow:hidden}
.product .shot{position:absolute;inset:0}
.product .band{position:absolute;left:0;right:0;bottom:0;height:30px;background:var(--card-band);display:flex;justify-content:center;align-items:center;gap:9px}
.product .band i{width:20px;height:18px;background:#fff;display:flex;align-items:center;justify-content:center}
.product .label{position:absolute;left:0;right:0;top:34px;text-align:center;font-family:"Josefin Sans",sans-serif;font-size:20px}

/* newsletter */
.news-title{left:0;width:776px;top:742px;text-align:center;font-family:"Roboto",sans-serif;font-weight:300;font-size:26px}
.news-sub{left:0;width:776px;top:780px;text-align:center;font-family:"Roboto",sans-serif;font-weight:300;font-size:14.5px}
.email{left:201px;top:824px;width:277px;height:30px;border:1px solid var(--ink);font-family:"Lato",sans-serif;font-size:8px;padding:0 9px;display:flex;align-items:center;color:var(--muted)}
.signup{left:477px;top:824px;width:112px;height:30px;background:var(--ink);color:#fff;font-family:"Roboto",sans-serif;font-weight:300;font-size:15px;display:flex;align-items:center;justify-content:center}

/* perks */
.perk{top:918px;display:flex;gap:9px}
.perk h4{font-size:9.5px;font-weight:700;margin-bottom:5px}
.perk p{font-size:7.6px;line-height:11px;color:#222}

/* footer */
.footer{left:0;top:985px;width:776px;height:185px;background:radial-gradient(ellipse at 55% 55%,#55524f 0%,var(--footer) 45%,#303032 100%)}
.foot-col{top:1013px;color:var(--footer-text)}
.foot-col h5{font-family:"Lato",sans-serif;font-weight:700;font-size:12px;color:#fff;margin-bottom:7px}
.foot-col .rule{width:18px;height:1px;background:#fff;margin-bottom:11px}
.foot-col p{font-size:7.9px;line-height:10.8px;color:#eee}
.foot-col ul{list-style:none}
.foot-col li{font-size:8px;line-height:16.7px;color:#eee}
.foot-col li::before{content:"›";margin-right:5px}
.contact{display:flex;align-items:center;gap:8px;font-size:8px;color:#eee;margin-top:6px}
.foot-brand{left:636px;top:1030px;font-family:"Josefin Sans",sans-serif;font-weight:700;font-size:38px;color:#cfcfcf;letter-spacing:-1px}
.social{top:1098px;width:19px;height:19px;border-radius:50%;border:1.5px solid var(--social)}
.bottom{left:0;top:1169px;width:776px;height:31px;background:var(--footer-deep);color:#eee;font-size:8.4px}
.card-badge{top:1178px;width:22px;height:13px;background:#f1f1f1;border-radius:1px}
</style>
</head>
<body>

<!-- hero -->
<section class="abs hero">
  <div class="abs hero-photo" role="img" aria-label="Woman in black sports bra and shorts holding a kneeling backbend yoga pose"></div>
  <div class="abs brand">Vessa</div>
  <div class="abs cart-link">View Cart (0)
    <svg width="15" height="13" viewBox="0 0 15 13"><path d="M0 1h3l2 7h8l2-6H4" fill="none" stroke="#111" stroke-width="1.6"/><path d="M4 2h11l-2 6H5z" fill="#111"/><circle cx="6" cy="11" r="1.3" fill="#111"/><circle cx="12" cy="11" r="1.3" fill="#111"/></svg>
  </div>
  <svg class="abs menu" width="15" height="12" viewBox="0 0 15 12"><rect width="15" height="2.4" fill="#111"/><rect y="4.8" width="15" height="2.4" fill="#111"/><rect y="9.6" width="15" height="2.4" fill="#111"/></svg>
  <div class="abs offer">
    <div class="pct">50%<small>off</small></div>
    <div class="line">Active Stretch Yoga</div>
    <div class="line">Tops &amp; Shorts</div>
  </div>
  <div class="abs buy">Buy Now</div>
  <div class="dots"><span class="on" style="left:328px"></span><span style="left:358px"></span><span style="left:390px"></span></div>
</section>

<!-- featured products -->
<h2 class="abs section-title">Featured Products</h2>
<div class="abs title-rule"></div>
<div class="abs pager" style="left:677px"><svg width="6" height="7"><path d="M6 0v7L0 3.5z" fill="#111"/></svg></div>
<div class="abs pager" style="left:695px"><svg width="6" height="7"><path d="M0 0v7l6-3.5z" fill="#111"/></svg></div>

<svg width="0" height="0" style="position:absolute">
  <defs>
    <symbol id="i-cart" viewBox="0 0 12 10"><path d="M0 1h2l1.6 5h6L11 2H3" fill="none" stroke="#111" stroke-width="1"/><circle cx="4.5" cy="8.5" r="1" fill="#111"/><circle cx="9" cy="8.5" r="1" fill="#111"/></symbol>
    <symbol id="i-heart" viewBox="0 0 12 10"><path d="M6 9.5L1.2 4.8A2.5 2.5 0 0 1 6 2a2.5 2.5 0 0 1 4.8 2.8z" fill="none" stroke="#111" stroke-width="1.1"/></symbol>
    <symbol id="i-swap" viewBox="0 0 12 10"><path d="M2 6V2.5h7M7.5 1 9.5 2.5 7.5 4M10 4v3.5H3M4.5 9 2.5 7.5 4.5 6" fill="none" stroke="#111" stroke-width="1.6"/></symbol>
    <symbol id="i-eye" viewBox="0 0 12 10"><path d="M0.5 5Q6-1 11.5 5Q6 11 0.5 5z" fill="#111"/><circle cx="6" cy="5" r="1.6" fill="#fff"/></symbol>
  </defs>
</svg>

<div class="abs product" style="left:65px;top:450px;width:174px;height:120px">
  <div class="shot" role="img" aria-label="White yoga shorts" style="background:radial-gradient(ellipse at 50% 45%,#ffffff 0%,#f3f3f4 40%,#e9e9eb 80%)"></div>
  <div class="label">Yoga Shorts</div>
  <div class="band"><i><svg width="12" height="10"><use href="#i-cart"/></svg></i><i><svg width="12" height="10"><use href="#i-heart"/></svg></i><i><svg width="12" height="10"><use href="#i-swap"/></svg></i><i><svg width="12" height="10"><use href="#i-eye"/></svg></i></div>
</div>

<div class="abs product" style="left:65px;top:584px;width:174px;height:120px">
  <div class="shot" role="img" aria-label="Turquoise racerback tank top" style="background:radial-gradient(ellipse 30% 50% at 50% 40%,#1fb9c0 0%,#31c0c6 60%,rgba(233,233,235,0) 100%),#e9e9eb"></div>
  <div class="band"><i><svg width="12" height="10"><use href="#i-cart"/></svg></i><i><svg width="12" height="10"><use href="#i-heart"/></svg></i><i><svg width="12" height="10"><use href="#i-swap"/></svg></i><i><svg width="12" height="10"><use href="#i-eye"/></svg></i></div>
</div>

<div class="abs product" style="left:254px;top:452px;width:269px;height:252px">
  <div class="shot" role="img" aria-label="Model shown from three angles in black sports bra and black and pink capri leggings" style="background:linear-gradient(90deg,rgba(0,0,0,0) 12%,rgba(40,40,44,.55) 20%,rgba(0,0,0,0) 28%,rgba(0,0,0,0) 41%,rgba(40,40,44,.55) 50%,rgba(0,0,0,0) 59%,rgba(0,0,0,0) 71%,rgba(40,40,44,.55) 79%,rgba(0,0,0,0) 87%),linear-gradient(180deg,#ececee,#dcdcdf)"></div>
  <div class="band"><i><svg width="12" height="10"><use href="#i-cart"/></svg></i><i><svg width="12" height="10"><use href="#i-heart"/></svg></i><i><svg width="12" height="10"><use href="#i-swap"/></svg></i><i><svg width="12" height="10"><use href="#i-eye"/></svg></i></div>
</div>

<div class="abs product" style="left:538px;top:452px;width:174px;height:120px">
  <div class="shot" role="img" aria-label="Black sports bra with lime dots" style="background:radial-gradient(ellipse 30% 40% at 50% 50%,#2a2a2c 0%,#333 60%,rgba(233,233,235,0) 100%),#e9e9eb"></div>
  <div class="band"><i><svg width="12" height="10"><use href="#i-cart"/></svg></i><i><svg width="12" height="10"><use href="#i-heart"/></svg></i><i><svg width="12" height="10"><use href="#i-swap"/></svg></i><i><svg width="12" height="10"><use href="#i-eye"/></svg></i></div>
</div>

<div class="abs product" style="left:538px;top:584px;width:174px;height:120px">
  <div class="shot" role="img" aria-label="Black mesh racerback sports bra" style="background:radial-gradient(ellipse 30% 45% at 50% 45%,#1e1e20 0%,#2c2c2e 60%,rgba(233,233,235,0) 100%),#e9e9eb"></div>
  <div class="band"><i><svg width="12" height="10"><use href="#i-cart"/></svg></i><i><svg width="12" height="10"><use href="#i-heart"/></svg></i><i><svg width="12" height="10"><use href="#i-swap"/></svg></i><i><svg width="12" height="10"><use href="#i-eye"/></svg></i></div>
</div>

<!-- newsletter -->
<h2 class="abs news-title">BE THE FIRST TO KNOW</h2>
<p class="abs news-sub">Sign up for the latest news, new releases and special promotions.</p>
<div class="abs email">Enter Your Email</div>
<div class="abs signup">Sign Up</div>

<!-- perks -->
<div class="abs perk" style="left:60px">
  <svg width="41" height="22" viewBox="0 0 41 22"><rect x="0" y="2" width="24" height="14" fill="#111"/><path d="M25 6h8l5 5v5H25z" fill="#111"/><rect x="28" y="8" width="4" height="3" fill="#fff"/><circle cx="8" cy="18" r="3" fill="#111" stroke="#fff"/><circle cx="32" cy="18" r="3" fill="#111" stroke="#fff"/></svg>
  <div><h4>Free Shipping</h4><p>Free shipping on all US orders</p></div>
</div>
<div class="abs perk" style="left:246px">
  <svg width="24" height="24" viewBox="0 0 24 24"><path d="M12 2a10 10 0 1 1-9.4 6.6" fill="none" stroke="#111" stroke-width="2"/><path d="M1 6l2 3 3-2" fill="none" stroke="#111" stroke-width="1.6"/><text x="12" y="15" text-anchor="middle" font-family="Lato,sans-serif" font-size="6.5" font-weight="700" fill="#111">24/7</text></svg>
  <div><h4>Suport 24/7</h4><p>We support our customers<br>24 hours a day</p></div>
</div>
<div class="abs perk" style="left:406px">
  <svg width="20" height="24" viewBox="0 0 20 24"><path d="M10 7C7 1 3 3 5 6M10 7c3-6 7-4 5-1" fill="none" stroke="#111" stroke-width="1.4"/><rect x="1" y="7" width="18" height="5" fill="#111"/><rect x="2.5" y="12" width="15" height="11" fill="#111"/><rect x="9" y="7" width="2" height="16" fill="#fff"/></svg>
  <div><h4>Gift Cards</h4><p>We have the perfect gift card<br>for you</p></div>
</div>
<div class="abs perk" style="left:572px">
  <svg width="34" height="22" viewBox="0 0 34 22"><rect x="1" y="1" width="32" height="20" rx="2" fill="none" stroke="#111" stroke-width="2"/><rect x="1" y="6" width="32" height="4" fill="#111"/><rect x="5" y="14" width="10" height="2" fill="#111"/></svg>
  <div><h4>Payment 100% secure</h4><p>We are trusted sellers</p></div>
</div>

<!-- footer -->
<footer class="abs footer" role="img" aria-label="Dim background of a yoga practitioner in an inverted pose"></footer>

<div class="abs foot-col" style="left:65px;width:200px">
  <h5>About Vessa</h5><div class="rule"></div>
  <p>Lorem ipsum dolor sit amet, consectetuer adipiscing elit, sed diam nonummy nibh euismod tincidunt ut laoreet dolore magna aliquam erat volutpat. Ut wisi enim ad minim veniam.</p>
  <div class="contact" style="margin-top:8px"><svg width="9" height="11" viewBox="0 0 9 11"><path d="M4.5 11C1.5 7 0 5.5 0 4a4.5 4.5 0 0 1 9 0c0 1.5-1.5 3-4.5 7z" fill="#fff"/><circle cx="4.5" cy="4" r="1.6" fill="#3b3b3d"/></svg>123 Lorem ipsum helps you lismarter</div>
  <div class="contact"><svg width="9" height="10" viewBox="0 0 9 10"><path d="M1 0h2l1 2.5-1.3 1a6 6 0 0 0 2.8 2.8l1-1.3L9 6v2c0 1-1 2-2 2A7 7 0 0 1 0 3c0-1 0-3 1-3z" fill="#fff"/></svg>123-456-7890</div>
  <div class="contact"><svg width="10" height="8" viewBox="0 0 10 8"><rect width="10" height="8" fill="#fff"/><path d="M0 0l5 4 5-4" fill="none" stroke="#3b3b3d"/></svg>info@vessa.example</div>
</div>

<div class="abs foot-col" style="left:322px">
  <h5>Quick Links</h5><div class="rule"></div>
  <ul><li>Home</li><li>About</li><li>Inspiration</li><li>Featured Products</li><li>Blog</li><li>Contact Us</li></ul>
</div>

<div class="abs foot-col" style="left:474px">
  <h5>Information</h5><div class="rule"></div>
  <ul><li>Customer Service</li><li>New Collection</li><li>Privacy Policy</li><li>Terms &amp; Condition</li><li>Blog</li></ul>
</div>

<div class="abs foot-brand">Vessa</div>
<div class="abs social" style="left:624px"></div>
<div class="abs social" style="left:647px"></div>
<div class="abs social" style="left:670px"></div>
<div class="abs social" style="left:694px;border-color:var(--social-alt)"></div>

<div class="abs bottom">
  <span class="abs" style="left:66px;top:11px">Copyright © 2016 Vessa. All Rights Reserved.</span>
  <span class="abs" style="left:533px;top:11px">We Accept :</span>
</div>
<div class="abs card-badge" style="left:586px"></div>
<div class="abs card-badge" style="left:612px"></div>
<div class="abs card-badge" style="left:638px"></div>
<div class="abs card-badge" style="left:664px"></div>
<div class="abs card-badge" style="left:690px"></div>

</body>
</html>
```